Stationary set for consulting company
Tarvo Bridge
Creative Brief
Modern
Karim Yusuf Al Banna
Co-Founder
Reef Spire, Abu Dhabi United Arab Emirates
karim@tarvobridge.ae
www.tarvobridge.com
I need a full stationary set for the company logo I will be attaching. (PPTs, business cards, envelope, letterhead, etc)

```html
<!DOCTYPE html>
<html lang="en">
<head>
<meta charset="utf-8">
<title>Tarvo Bridge Stationery Set</title>
<link href="https://fonts.googleapis.com/css2?family=Montserrat:wght@400;500;600&display=swap" rel="stylesheet">
<style>
  :root {
    --navy: #1d3a82;
    --navy-deep: #1a3478;
    --sky: #7fb0de;
    --ink: #4a5670;
    --muted: #8a93a6;
    --paper: #ffffff;
    --backdrop: #eceef2;
    --line: #d7dce6;
  }
  * { box-sizing: border-box; margin: 0; padding: 0; }
  html, body { width: 1200px; height: 502px; overflow: hidden; }
  body {
    background: var(--backdrop);
    font-family: "Montserrat", Arial, sans-serif;
    color: var(--ink);
    position: relative;
  }
  .sheet { position: absolute; background: var(--paper); box-shadow: 0 2px 6px rgba(20,30,60,.12); overflow: hidden; }

  .brand { display: flex; align-items: center; gap: 5px; color: var(--navy); font-weight: 600; letter-spacing: .04em; white-space: nowrap; }
  .brand-dot { background: var(--sky); border-radius: 50%; flex: none; }

  /* business card front */
  .card-front { left: 48px; top: 30px; width: 510px; height: 210px; }
  .card-front .brand { position: absolute; left: 50%; top: 26px; transform: translateX(-50%); font-size: 15px; }
  .card-front .brand-dot { width: 9px; height: 9px; }
  .card-front .rule { position: absolute; left: 205px; right: 205px; top: 58px; border-top: 1px solid var(--line); }
  .card-name { position: absolute; top: 82px; width: 100%; text-align: center; font-size: 13px; font-weight: 500; letter-spacing: .12em; text-transform: uppercase; color: var(--navy); }
  .card-title { position: absolute; top: 102px; width: 100%; text-align: center; font-size: 9px; color: var(--sky); }
  .card-contacts { position: absolute; top: 140px; left: 108px; right: 60px; display: grid; grid-template-columns: 1fr 1fr; row-gap: 7px; column-gap: 30px; font-size: 7.5px; color: var(--navy); }
  .contact { display: flex; align-items: flex-start; gap: 6px; line-height: 1.3; }
  .contact svg { flex: none; width: 9px; height: 9px; }
  .card-band { position: absolute; left: 0; right: 0; bottom: 0; height: 8px; background: var(--sky); }

  /* business card back */
  .card-back { left: 48px; top: 270px; width: 510px; height: 210px; background: var(--navy-deep); }
  .card-back .watermark { position: absolute; left: 40px; bottom: 30px; font-size: 40px; font-weight: 600; color: rgba(255,255,255,.12); letter-spacing: .04em; white-space: nowrap; }

  /* letterhead */
  .letterhead { left: 600px; top: 30px; width: 290px; height: 450px; }
  .letterhead .top-band { position: absolute; left: 0; right: 0; top: 0; height: 4px; background: var(--sky); }
  .letterhead .brand { position: absolute; left: 50%; top: 16px; transform: translateX(-50%); font-size: 9px; }
  .letterhead .brand-dot { width: 5px; height: 5px; }
  .letter-body { position: absolute; left: 32px; right: 32px; top: 62px; font-size: 5.2px; line-height: 1.75; color: var(--ink); }
  .letter-body p { margin-bottom: 8px; }
  .signature { width: 40px; height: 12px; margin: 10px 0 3px; background: linear-gradient(90deg, #9aa3b8, #c4cad6); border-radius: 6px; }
  .letter-footer { position: absolute; left: 20px; right: 20px; bottom: 12px; display: flex; justify-content: space-between; font-size: 4.4px; color: var(--navy); }
  .letter-footer span { display: flex; align-items: center; gap: 3px; }
  .letter-footer svg { width: 5px; height: 5px; }

  /* envelopes */
  .envelope { left: 915px; width: 262px; height: 200px; }
  .envelope-front { top: 35px; }
  .envelope-front .top-band { position: absolute; left: 0; right: 0; top: 0; height: 5px; background: var(--sky); }
  .envelope-front .brand { position: absolute; left: 50%; top: 20px; transform: translateX(-50%); font-size: 10px; }
  .envelope-front .brand-dot { width: 6px; height: 6px; }
  .envelope-back { top: 278px; }
  .envelope-back svg.flaps { position: absolute; inset: 0; }
  .envelope-back .brand { position: absolute; left: 50%; top: 84px; transform: translateX(-50%); font-size: 9px; }
  .envelope-back .brand-dot { width: 5px; height: 5px; }
</style>
</head>
<body>

<section class="sheet card-front">
  <div class="brand"><span class="brand-dot"></span>Tarvo Bridge</div>
  <div class="rule"></div>
  <div class="card-name">Karim Yusuf Al Banna</div>
  <div class="card-title">Co-Founder</div>
  <div class="card-contacts">
    <div class="contact">
      <svg viewBox="0 0 10 10"><path d="M2 1l2 2-1 1.5c.7 1.3 1.6 2.2 2.9 2.9L7.4 6l2 2-1.4 1.5C4.5 9 1 5.5.5 2z" fill="none" stroke="#7fb0de" stroke-width=".9"/></svg>
      <span>+971-50-4417390</span>
    </div>
    <div class="contact">
      <svg viewBox="0 0 10 10"><circle cx="5" cy="5" r="4" fill="none" stroke="#7fb0de" stroke-width=".9"/><path d="M1 5h8M5 1c2 2.4 2 5.6 0 8M5 1c-2 2.4-2 5.6 0 8" fill="none" stroke="#7fb0de" stroke-width=".7"/></svg>
      <span>www.tarvobridge.com</span>
    </div>
    <div class="contact">
      <svg viewBox="0 0 10 10"><rect x="1" y="2" width="8" height="6" fill="none" stroke="#7fb0de" stroke-width=".9"/><path d="M1 2l4 3.5L9 2" fill="none" stroke="#7fb0de" stroke-width=".9"/></svg>
      <span>karim@tarvobridge.ae</span>
    </div>
    <div class="contact">
      <svg viewBox="0 0 10 10"><path d="M5 9.5S1.8 6 1.8 3.8a3.2 3.2 0 016.4 0C8.2 6 5 9.5 5 9.5z" fill="none" stroke="#7fb0de" stroke-width=".9"/><circle cx="5" cy="3.8" r="1.1" fill="#7fb0de"/></svg>
      <span>Reef Spire, Abu Dhabi<br>United Arab Emirates</span>
    </div>
  </div>
  <div class="card-band"></div>
</section>

<section class="sheet card-back">
  <div class="watermark">Tarvo Bridge</div>
</section>

<section class="sheet letterhead">
  <div class="top-band"></div>
  <div class="brand"><span class="brand-dot"></span>Tarvo Bridge</div>
  <div class="letter-body">
    <p>Dear Mr. Hale,</p>
    <p>Thank you for meeting with our team last week. We were glad to learn more about your plans for the coming year and the goals you shared with us.</p>
    <p>Our consultants have reviewed the notes from that session and prepared a short outline of the next steps we suggest for your operations and staff.</p>
    <p>Please find the full proposal enclosed. We would be happy to walk you through each section at a time that suits you.</p>
    <p>We look forward to working together.</p>
    <div class="signature" role="img" aria-label="Handwritten signature"></div>
    <p>Sincerely,</p>
  </div>
  <div class="letter-footer">
    <span><svg viewBox="0 0 10 10"><circle cx="5" cy="5" r="4.5" fill="#7fb0de"/></svg>+971-50-4417390</span>
    <span><svg viewBox="0 0 10 10"><circle cx="5" cy="5" r="4.5" fill="#7fb0de"/></svg>karim@tarvobridge.ae</span>
    <span><svg viewBox="0 0 10 10"><circle cx="5" cy="5" r="4.5" fill="#7fb0de"/></svg>www.tarvobridge.com</span>
    <span><svg viewBox="0 0 10 10"><circle cx="5" cy="5" r="4.5" fill="#7fb0de"/></svg>Reef Spire, Abu Dhabi</span>
  </div>
</section>

<section class="sheet envelope envelope-front">
  <div class="top-band"></div>
  <div class="brand"><span class="brand-dot"></span>Tarvo Bridge</div>
</section>

<section class="sheet envelope envelope-back">
  <svg class="flaps" viewBox="0 0 262 200" preserveAspectRatio="none">
    <path d="M0 0L131 110L262 0" fill="none" stroke="#d7dce6" stroke-width="1"/>
    <path d="M0 200L110 95M262 200L152 95" fill="none" stroke="#e3e7ee" stroke-width="1"/>
  </svg>
  <div class="brand"><span class="brand-dot"></span>Tarvo Bridge</div>
</section>

</body>
</html>
```